HTML Email Signature Design for Consulting Firm

We need an eamil signature design for an environmental consulting firm. The signature should be the best we can find in the market for a consulting firm in professional terms.

The design should include the following social media sites:

-Pelmosta
-Quibrel
- Gromvale

It is important that the signature is visually appealing alonside our logo.

Instructions on how to insert the signature within Microsoft Outlook are desirable as part of the deliverables.

The main reason we need HTML is that a recipient of our emails should be able to copy information from the signature and use it on the web etc..

Target Market(s)

private and public cleints

Industry/Entity Type

Environmental Consultant

Requirements
Must have
• Professional appeal ; Color combination blends nicely with Logo
Nice to have
• Blend nicely with Logo
Should not have
• No shadows in design

```html
<!DOCTYPE html>
<html lang="en">
<head>
<meta charset="utf-8">
<title>Verdantiq Email Signature</title>
<link href="https://fonts.googleapis.com/css2?family=Lato:wght@400;700;900&display=swap" rel="stylesheet">
<style>
  :root {
    --ink: #373d5a;
    --teal: #1a8ca6;
    --divider: #22a9c8;
    --social: #c9c9c9;
    --social-text: #9a9a9a;
    --mark: #5db332;
    --band-orange: #f6a21a;
    --band-yellow: #e9d21f;
    --band-green: #5fc23a;
    --band-deep-green: #1ea35a;
    --band-cyan: #19b8d6;
    --band-blue: #1f8fcf;
    --paper: #ffffff;
  }
  html, body {
    margin: 0;
    padding: 0;
    overflow: hidden;
    background: var(--paper);
  }
  .signature {
    position: relative;
    width: 1200px;
    height: 500px;
    overflow: hidden;
    background: var(--paper);
    font-family: "Lato", sans-serif;
  }
  .brand-mark {
    position: absolute;
    left: 50px;
    top: 170px;
    width: 240px;
    height: 60px;
    display: flex;
    align-items: center;
    justify-content: center;
    gap: 12px;
  }
  .brand-mark__dot {
    width: 30px;
    height: 30px;
    border-radius: 50%;
    background: var(--mark);
  }
  .brand-mark__name {
    font-size: 32px;
    font-weight: 700;
    color: var(--mark);
  }
  .divider {
    position: absolute;
    left: 323px;
    top: 36px;
    width: 3px;
    height: 374px;
    background: var(--divider);
  }
  .details {
    position: absolute;
    left: 374px;
    top: 60px;
  }
  .person {
    margin: 0;
    font-size: 34px;
    line-height: 44px;
    white-space: nowrap;
  }
  .person__name {
    font-weight: 700;
    color: var(--ink);
  }
  .person__role {
    font-weight: 400;
    color: var(--teal);
    margin-left: 12px;
  }
  .company {
    margin: 44px 0 0;
    font-size: 48px;
    line-height: 56px;
    font-weight: 900;
    letter-spacing: 2px;
    color: var(--ink);
  }
  .contact {
    margin: 14px 0 0;
    padding: 0;
    list-style: none;
    font-size: 22px;
    line-height: 38px;
    color: var(--teal);
  }
  .social {
    position: absolute;
    left: 376px;
    top: 366px;
    display: flex;
    gap: 34px;
    margin: 0;
    padding: 0;
    list-style: none;
  }
  .social__item {
    display: flex;
    align-items: center;
    gap: 10px;
    font-size: 20px;
    font-weight: 700;
    color: var(--social-text);
  }
  .social__dot {
    width: 40px;
    height: 40px;
    border-radius: 50%;
    background: var(--social);
  }
  .color-band {
    position: absolute;
    left: 0;
    bottom: 0;
    width: 1200px;
    height: 44px;
    background: linear-gradient(90deg,
      var(--band-orange) 0%,
      var(--band-yellow) 28%,
      var(--band-green) 50%,
      var(--band-deep-green) 66%,
      var(--band-cyan) 82%,
      var(--band-blue) 100%);
  }
  .color-band::after {
    content: "";
    position: absolute;
    inset: 0;
    background: linear-gradient(180deg, rgba(255,255,255,0.85) 0%, rgba(255,255,255,0) 60%);
  }
</style>
</head>
<body>
  <div class="signature">
    <div class="brand-mark">
      <span class="brand-mark__dot"></span>
      <span class="brand-mark__name">Verdantiq</span>
    </div>

    <div class="divider"></div>

    <div class="details">
      <p class="person">
        <span class="person__name">Morgan Ellery</span>
        <span class="person__role">• Excecutive Assistant</span>
      </p>
      <h1 class="company">VERDANTIQ</h1>
      <ul class="contact">
        <li class="contact__address">27 Harbour Lane&nbsp; Kingsford, Ontario</li>
        <li class="contact__phone">Phone : +1 800 555 0142</li>
        <li class="contact__email">Email : morgan@verdantiq.com</li>
      </ul>
    </div>

    <ul class="social">
      <li class="social__item"><span class="social__dot"></span>Gromvale</li>
      <li class="social__item"><span class="social__dot"></span>Quibrel</li>
      <li class="social__item"><span class="social__dot"></span>Pelmosta</li>
    </ul>

    <div class="color-band"></div>
  </div>
</body>
</html>
```